Website design for Halvard Remit

We need a website design based upon the Halvard Remit look-and-feel. Halvard Remit is all about connecting in the dynamic and fast moving world of (internet and mobile) payments. Our logo and colors (dark blue, grey and white) reflect this. The font we use is " Museo". See attached files. Our website needs to be responsive to the screen of the device used. Preferably based upon the wordpress theme, which supports many widgets and is open source:
http://layoutbazaar.example/item/sole-adaptive-layered-site-template/8163049. Please share your thoughts, suggestions and proposal and let me know what you need me to do or share with you to make this happen. Thanks. Maarten.

Industry/Entity Type

Internet

```html
<!DOCTYPE html>
<html lang="en">
<head>
<meta charset="utf-8">
<title>Halvard Remit</title>
<link href="https://fonts.googleapis.com/css2?family=Lato:wght@300;400;700&family=Open+Sans:wght@400;600;700&display=swap" rel="stylesheet">
<style>
  :root {
    --navy: #0d5a86;
    --navy-deep: #0a4a70;
    --blue: #1a8ac6;
    --grey-bar: #9b9b9b;
    --grey-band: #ababab;
    --page: #e9e9e9;
    --white: #ffffff;
    --footer: #f6f6f6;
    --text: #7a7a7a;
    --text-soft: #9a9a9a;
  }
  html, body { margin: 0; padding: 0; width: 832px; height: 1200px; overflow: hidden; }
  body { background: var(--page); font-family: "Open Sans", sans-serif; color: var(--text); }
  .stage { position: relative; width: 832px; height: 1200px; overflow: hidden; }
  .abs { position: absolute; }

  /* header */
  .topline { left: 0; top: 0; width: 832px; height: 5px; background: var(--navy); }
  .navbar { left: 0; top: 5px; width: 832px; height: 48px; background: var(--grey-bar); }
  .nav-link { top: 27px; font-size: 8px; font-weight: 600; letter-spacing: .8px; color: var(--white); text-transform: uppercase; }
  .brand-tab { left: 342px; top: 5px; width: 138px; height: 48px; background: var(--navy); text-align: center; color: var(--white); }
  .brand-name { padding-top: 25px; font-size: 10px; line-height: 12px; font-weight: 400; }

  /* hero */
  .column { left: 122px; width: 574px; background: var(--white); }
  .hero-photo { left: 122px; top: 53px; width: 574px; height: 247px;
    background: radial-gradient(ellipse at 70% 50%, #5fb6e6 0%, #1f6fa8 35%, #0c2f55 75%, #071c36 100%); }
  .hero-panel { left: 122px; top: 82px; width: 202px; height: 192px; background: rgba(40,50,60,.72); }
  .hero-title { left: 170px; top: 106px; width: 150px; font-size: 10.5px; font-weight: 700; line-height: 12px; color: var(--white); text-transform: uppercase; }
  .hero-copy { left: 170px; top: 136px; width: 128px; font-size: 6.5px; line-height: 9px; color: #dfe7ee; }
  .hero-btn { left: 168px; top: 186px; width: 67px; height: 17px; background: var(--navy); color: var(--white); font-size: 6.5px; line-height: 17px; text-align: center; }
  .hero-dots { left: 198px; top: 227px; }

  /* features */
  .feature { top: 324px; width: 130px; }
  .feature h2 { margin: 0 0 18px; font-size: 14px; line-height: 16px; font-weight: 700; color: var(--blue); }
  .feature p { margin: 0; font-size: 7.5px; line-height: 10px; color: var(--text); }
  .rule { left: 122px; top: 440px; width: 574px; height: 1px; background: #d8d8d8; }
  .tagline { left: 139px; top: 461px; width: 322px; font-family: "Lato", sans-serif; font-weight: 300; font-size: 13.5px; line-height: 17px; color: #808080; }
  .fees-btn { left: 499px; top: 462px; width: 173px; height: 31px; background: var(--blue); color: var(--white); font-size: 14px; line-height: 31px; text-align: center; box-shadow: 0 2px 3px rgba(0,0,0,.35); }
  .section-title { left: 122px; width: 574px; text-align: center; font-family: "Lato", sans-serif; font-size: 13px; letter-spacing: 1.2px; color: var(--navy); text-transform: uppercase; }

  /* how it works */
  .how-photo { left: 0; top: 592px; width: 832px; height: 160px;
    background: linear-gradient(90deg, #1b3a66 0%, #3b6ea8 18%, #a9c7e6 45%, #5d8fc6 65%, #2c4f8a 82%, #c24a5a 100%); }
  .step { top: 592px; width: 132px; height: 160px; background: rgba(13,90,134,.92); text-align: center; color: var(--white); }
  .step svg { display: block; margin: 13px auto 0; }
  .step h3 { margin: 6px 0 5px; font-size: 8px; font-weight: 700; }
  .step p { margin: 0 12px; font-size: 5.6px; line-height: 7.5px; text-align: left; color: #d4e4ef; }

  /* clients */
  .clients-band { left: 128px; top: 800px; width: 561px; height: 62px; background: var(--grey-band); }
  .client { top: 822px; width: 90px; text-align: center; font-size: 13px; font-weight: 700; color: var(--white); }

  /* location */
  .map { left: 128px; top: 924px; width: 566px; height: 100px; background: linear-gradient(135deg, #dfe6d8 0%, #cfdcc8 45%, #a9c9e8 70%, #c8d6e6 100%); }

  /* footer */
  .footer { left: 0; top: 1050px; width: 832px; height: 114px; background: var(--footer); }
  .field { left: 134px; width: 162px; height: 11px; border: 1px solid #b8b8b8; background: var(--white); font-size: 5px; line-height: 9px; padding-left: 3px; color: #b0b0b0; box-sizing: border-box; }
  .message { left: 316px; top: 1081px; width: 163px; height: 30px; border: 1px solid #b8b8b8; background: var(--white); font-size: 5px; padding: 2px 3px; color: #b0b0b0; box-sizing: border-box; }
  .send { left: 316px; top: 1117px; width: 163px; height: 11px; background: var(--navy); color: var(--white); font-size: 5.5px; letter-spacing: 1.5px; line-height: 11px; text-align: center; }
  .footer-head { top: 1081px; font-size: 6px; font-weight: 700; color: var(--navy); text-transform: uppercase; }
  .footer-list { top: 1091px; margin: 0; padding: 0; list-style: none; font-size: 6px; line-height: 8px; color: var(--text); }
  .copybar { left: 0; top: 1164px; width: 832px; height: 36px; background: var(--navy); }
  .copyright { left: 0; top: 1177px; width: 832px; text-align: center; font-family: "Lato", sans-serif; font-size: 8.5px; color: #b8cfdf; }
</style>
</head>
<body>
<div class="stage">

  <header>
    <div class="abs topline"></div>
    <nav class="abs navbar"></nav>
    <span class="abs nav-link" style="left:139px">Home</span>
    <span class="abs nav-link" style="left:209px">Services</span>
    <span class="abs nav-link" style="left:288px">Fees</span>
    <div class="abs brand-tab">
      <div class="brand-name">Halvard Remit</div>
    </div>
    <span class="abs nav-link" style="left:498px">Contact us</span>
    <span class="abs nav-link" style="left:588px">FAQ</span>
    <span class="abs nav-link" style="left:644px">Support</span>
  </header>

  <div class="abs column" style="top:300px;height:292px"></div>
  <div class="abs column" style="top:752px;height:298px"></div>

  <section class="hero">
    <div class="abs hero-photo" role="img" aria-label="Photo of a hand holding a smartphone surrounded by glowing payment icons on a blue background"></div>
    <div class="abs hero-panel"></div>
    <div class="abs hero-title">Mobile payments wherever you are!</div>
    <div class="abs hero-copy">Send and receive money from any phone in seconds. One secure account links your cards, wallets and bank so every payment stays simple and clear.</div>
    <div class="abs hero-btn">More about this</div>
    <svg class="abs hero-dots" width="40" height="6" viewBox="0 0 40 6" aria-hidden="true">
      <circle cx="3" cy="3" r="2.5" fill="#fff"/>
      <circle cx="13" cy="3" r="2.5" fill="#1a8ac6"/>
      <circle cx="23" cy="3" r="2.5" fill="#1a8ac6"/>
      <circle cx="33" cy="3" r="2.5" fill="#1a8ac6"/>
    </svg>
  </section>

  <section class="features">
    <div class="abs feature" style="left:134px"><h2>Quick and easy Payments</h2><p>Open an account in minutes and start paying with a single tap.</p></div>
    <div class="abs feature" style="left:278px"><h2>Easy and Secure</h2><p>Every transfer is encrypted and checked before it leaves your hands.</p></div>
    <div class="abs feature" style="left:422px"><h2>24/7 support</h2><p>Our team answers day and night, by phone, chat or email.</p></div>
    <div class="abs feature" style="left:566px"><h2>Quality</h2><p>Clear fees, fast settlement and a service you can rely on.</p></div>
    <div class="abs rule"></div>
  </section>

  <section class="pitch">
    <p class="abs tagline" style="margin:0">We take away the hassel out of the payments so that you can focus on what is important.</p>
    <div class="abs fees-btn">Our Fees</div>
    <svg class="abs" style="left:196px;top:506px" width="426" height="22" viewBox="0 0 426 22" aria-hidden="true">
      <line x1="0" y1="11" x2="202" y2="11" stroke="#c8c8c8"/>
      <line x1="224" y1="11" x2="426" y2="11" stroke="#c8c8c8"/>
      <circle cx="213" cy="11" r="10" fill="#fff" stroke="#b5b5b5"/>
    </svg>
    <div class="abs section-title" style="top:550px">How it works</div>
  </section>

  <section class="how">
    <div class="abs how-photo" role="img" aria-label="Blurred photo of blue and red city lights"></div>

    <div class="abs step" style="left:122px">
      <svg width="38" height="38" viewBox="0 0 38 38" aria-hidden="true">
        <circle cx="19" cy="19" r="18" fill="#fff"/>
        <rect x="13" y="9" width="12" height="20" rx="2" fill="#0d5a86"/>
        <rect x="15" y="12" width="8" height="13" fill="#fff"/>
        <circle cx="19" cy="27" r="1" fill="#fff"/>
      </svg>
      <h3>Anywhere - Anytime</h3>
      <p>Pay from your phone, tablet or laptop wherever you are. Transfers settle in seconds, around the clock, in more than forty currencies. No queues, no paperwork, no waiting for the bank to open.</p>
    </div>

    <div class="abs step" style="left:270px">
      <svg width="38" height="38" viewBox="0 0 38 38" aria-hidden="true">
        <circle cx="19" cy="19" r="18" fill="#fff"/>
        <rect x="9" y="12" width="20" height="14" rx="2" fill="#0d5a86"/>
        <rect x="9" y="15" width="20" height="3" fill="#fff"/>
        <rect x="12" y="21" width="7" height="2" fill="#fff"/>
      </svg>
      <h3>Credit Card</h3>
      <p>Link any debit or credit card to your account once and use it everywhere. Cards are stored safely and can be paused or removed with a single tap in the app.</p>
    </div>

    <div class="abs step" style="left:416px">
      <svg width="38" height="38" viewBox="0 0 38 38" aria-hidden="true">
        <circle cx="19" cy="19" r="18" fill="#fff"/>
        <circle cx="19" cy="19" r="11" fill="none" stroke="#0d5a86" stroke-width="2"/>
        <path d="M10 15 Q19 21 28 15 M10 23 Q19 17 28 23 M19 8 Q13 19 19 30" fill="none" stroke="#0d5a86" stroke-width="1.6"/>
      </svg>
      <h3>Connected</h3>
      <p>Connect shops, friends and suppliers on one network. Send a request, share a link or scan a code, and the money moves straight to the right place without delay.</p>
    </div>

    <div class="abs step" style="left:564px">
      <svg width="38" height="38" viewBox="0 0 38 38" aria-hidden="true">
        <path d="M19 3 L33 8 V18 C33 27 26 33 19 36 C12 33 5 27 5 18 V8 Z" fill="#fff"/>
        <path d="M12 19 L17 24 L26 14" fill="none" stroke="#0d5a86" stroke-width="3"/>
      </svg>
      <h3>Protected</h3>
      <p>Every payment is guarded by encryption, fraud checks and two-step sign-in. If something looks wrong we stop it first and let you know right away.</p>
    </div>
  </section>

  <section class="clients">
    <div class="abs section-title" style="top:774px">Our clients</div>
    <div class="abs clients-band"></div>
    <span class="abs client" style="left:128px">Voxlyn</span>
    <span class="abs client" style="left:220px">Quartzline</span>
    <span class="abs client" style="left:313px">Voxlyn</span>
    <span class="abs client" style="left:405px">Quartzline</span>
    <span class="abs client" style="left:498px">Voxlyn</span>
    <span class="abs client" style="left:590px">Quartzline</span>
  </section>

  <section class="location">
    <div class="abs section-title" style="top:894px">Our location</div>
    <div class="abs map" role="img" aria-label="Street map around 1820 Larkspur Way, Fernhill, with the office marked by a pin"></div>
  </section>

  <footer>
    <div class="abs footer"></div>
    <div class="abs field" style="top:1081px">Name</div>
    <div class="abs field" style="top:1100px">Email Address</div>
    <div class="abs field" style="top:1118px">Subject</div>
    <div class="abs message">Message</div>
    <div class="abs send">SEND MESSAGE</div>

    <div class="abs footer-head" style="left:509px">Information</div>
    <ul class="abs footer-list" style="left:509px">
      <li>About Us</li>
      <li>Delivery Information</li>
      <li>Privacy Policy</li>
      <li>Terms &amp; Conditions</li>
    </ul>

    <div class="abs footer-head" style="left:602px">Online support</div>
    <ul class="abs footer-list" style="left:623px">
      <li>1-800-555-0142</li>
      <li>1-800-555-0187</li>
    </ul>
    <svg class="abs" style="left:602px;top:1116px" width="68" height="14" viewBox="0 0 68 14" aria-hidden="true">
      <circle cx="7" cy="7" r="6" fill="#0d5a86"/>
      <circle cx="20.5" cy="7" r="6" fill="#0d5a86"/>
      <circle cx="34" cy="7" r="6" fill="#0d5a86"/>
      <circle cx="47.5" cy="7" r="6" fill="#0d5a86"/>
      <circle cx="61" cy="7" r="6" fill="#0d5a86"/>
    </svg>

    <div class="abs copybar"></div>
    <div class="abs copyright">Copyright © 2014 Halvard Remit Inc. call (212) 555-0163 or email us</div>
  </footer>

</div>
</body>
</html>
```